School Management website

I need page design for our school management system website

Base website is www.brindavo.com. When the student logs in, he will reach the below pages.
You can either design with white and blue background or grey and white background

Page 1 - School Info

Header
product name("Brindavo") in left corner
logout link in right corner

LeftMenu

Dashboard
School Info
School Settings
Staffs
Classes
Messaging
Contact Us

Footer
About link and copyright text

School Info content
The page should have breadcrumb

The content of this page will be the school profile
We have to show the school logo
Name
School Type
School Code
School Count
School Address
School phone 1&2
School Email
School Website

The page content should show edit school profile link which will take the user to another page

```html
<!DOCTYPE html>
<html lang="en">
<head>
<meta charset="utf-8">
<title>Brindavo – School Info</title>
<link href="https://fonts.googleapis.com/css2?family=Open+Sans:wght@300;400;600&family=Roboto+Condensed:wght@400&display=swap" rel="stylesheet">
<style>
:root{
  --blue:#25a5de;
  --blue-dark:#1f96cc;
  --text:#777;
  --text-soft:#8a8a8a;
  --title:#2a9fd8;
  --line:#ececec;
  --panel-head:#f8f8f8;
  --page:#ffffff;
  --header-bg:#fafafa;
  --footer:#2b2b2b;
  --footer-text:#9a9a9a;
}
*{box-sizing:border-box;margin:0;padding:0}
html,body{width:1190px;height:1200px;overflow:hidden;background:var(--page);font-family:"Open Sans",Arial,sans-serif;color:var(--text)}
.site-header{position:absolute;left:0;top:0;width:1190px;height:110px;background:var(--header-bg);border-bottom:1px solid var(--line)}
.brand{position:absolute;left:171px;top:40px;display:flex;align-items:center;gap:8px;font-size:28px;font-weight:600;color:var(--blue)}
.brand-square{width:18px;height:18px;background:var(--blue)}
.header-tools{position:absolute;left:930px;top:0;height:110px;display:flex;align-items:center}
.user-menu{display:flex;align-items:center;gap:14px;padding-right:20px;height:110px;border-right:1px solid var(--line)}
.search{padding-left:22px}
.hero{position:absolute;left:171px;top:129px;width:850px;height:213px;background:linear-gradient(100deg,#f4f4f4 0%,#e6b59a 22%,#f1f1f1 45%,#e9e9e9 70%,#cfcfcf 100%)}
.sidebar{position:absolute;left:172px;top:368px;width:211px}
.nav-item{display:flex;height:45px}
.nav-icon{width:51px;background:var(--blue);display:flex;align-items:center;justify-content:center;border-bottom:1px solid var(--blue-dark)}
.nav-label{flex:1;background:#fafafa;border-bottom:1px solid var(--line);display:flex;align-items:center;padding-left:23px;font-size:16px;font-weight:300;color:var(--text-soft)}
.sidebar-contact{background:var(--blue);height:192px;padding-top:24px;font-family:"Roboto Condensed",Arial,sans-serif;color:#fff;font-size:13px;line-height:17px}
.contact-row{display:flex;margin-bottom:22px}
.contact-row .ic{width:55px;display:flex;justify-content:center;padding-top:2px}
.school-card{position:absolute;left:408px;width:613px}
.card-head{height:47px;background:var(--panel-head);border:1px solid var(--line);display:flex;align-items:center;justify-content:space-between;padding:0 16px 0 21px}
.card-title{font-size:16px;color:var(--title)}
.edit-link{display:flex;align-items:center;gap:18px;font-size:16px;font-weight:300;color:var(--text-soft)}
.card-body{position:relative;margin-top:4px;height:291px;border:1px solid var(--line);padding:27px 0 0 21px}
.info-row{display:flex;height:31.5px;font-size:12px;font-weight:300}
.info-row dt{width:135px;color:var(--text)}
.info-row .sep{width:35px}
.info-row dd{color:var(--text)}
.card-logo{position:absolute;right:30px;top:50px;display:flex;align-items:center;gap:8px;font-size:26px;font-weight:600;color:var(--blue)}
.card-logo.alt{color:#2a3f7a;font-size:22px}
.card-logo .sq{width:16px;height:16px;background:currentColor}
.site-footer{position:absolute;left:0;top:1106px;width:1190px;height:94px;background:var(--footer);color:var(--footer-text);font-size:12px;font-weight:300}
.copyright{position:absolute;left:171px;top:24px}
.footer-links{position:absolute;left:171px;top:58px;font-size:11px}
.footer-links a{color:var(--footer-text);text-decoration:none}
.footer-links span{margin:0 8px}
.social{position:absolute;left:933px;top:45px;display:flex;gap:14px}
.social i{width:12px;height:12px;border-radius:50%;background:#5a5a5a;display:block}
</style>
</head>
<body>
<header class="site-header">
  <div class="brand"><span class="brand-square"></span>Brindavo</div>
  <div class="header-tools">
    <div class="user-menu">
      <svg width="14" height="14" viewBox="0 0 14 14"><circle cx="7" cy="4" r="3.5" fill="#999"/><path d="M0 14c0-4 3-6 7-6s7 2 7 6z" fill="#999"/></svg>
      <svg width="9" height="7" viewBox="0 0 9 7"><path d="M0 0h9L4.5 7z" fill="#999"/></svg>
    </div>
    <div class="search"><svg width="15" height="15" viewBox="0 0 15 15"><circle cx="6" cy="6" r="5" fill="none" stroke="#999" stroke-width="1.6"/><path d="M10 10l4 4" stroke="#999" stroke-width="1.8"/></svg></div>
  </div>
</header>

<div class="hero" role="img" aria-label="Photo of a finger pressing a login key on a white laptop keyboard"></div>

<nav class="sidebar">
  <div class="nav-item"><div class="nav-icon"><svg width="20" height="16" viewBox="0 0 20 16" fill="#fff"><rect y="1" width="20" height="2"/><rect y="7" width="20" height="2"/><rect y="13" width="20" height="2"/></svg></div><div class="nav-label">Dashboard</div></div>
  <div class="nav-item"><div class="nav-icon"><svg width="20" height="20" viewBox="0 0 20 20" fill="none" stroke="#fff" stroke-width="2"><path d="M10 3H2v15h15v-8"/><path d="M8 12l1-4 8-7 3 3-8 7z" fill="#fff"/></svg></div><div class="nav-label">School Info</div></div>
  <div class="nav-item"><div class="nav-icon"><svg width="20" height="20" viewBox="0 0 20 20"><circle cx="10" cy="10" r="7" fill="none" stroke="#fff" stroke-width="4" stroke-dasharray="3 2.5"/><circle cx="10" cy="10" r="5.5" fill="none" stroke="#fff" stroke-width="2"/></svg></div><div class="nav-label">School Settings</div></div>
  <div class="nav-item"><div class="nav-icon"><svg width="16" height="18" viewBox="0 0 16 18" fill="#fff"><circle cx="8" cy="5" r="4"/><path d="M0 18c0-5 3-8 8-8s8 3 8 8z"/></svg></div><div class="nav-label">Staffs</div></div>
  <div class="nav-item"><div class="nav-icon"><svg width="20" height="20" viewBox="0 0 20 20" fill="none" stroke="#fff" stroke-width="1.8"><circle cx="10" cy="10" r="8.5"/><path d="M10 5v5h4"/></svg></div><div class="nav-label">Classes</div></div>
  <div class="nav-item"><div class="nav-icon"><svg width="22" height="20" viewBox="0 0 22 20" fill="#fff"><ellipse cx="9" cy="8" rx="8" ry="6"/><path d="M3 12l-1 5 5-3z"/><ellipse cx="15" cy="12" rx="6" ry="4.5" stroke="#25a5de" stroke-width="1.2"/></svg></div><div class="nav-label">Messaging</div></div>
  <div class="nav-item"><div class="nav-icon"><svg width="20" height="16" viewBox="0 0 20 16" fill="none" stroke="#fff" stroke-width="1.8"><rect x="1" y="1" width="18" height="14"/><path d="M1 1l9 8 9-8M1 15l7-6M19 15l-7-6"/></svg></div><div class="nav-label">Contact Us</div></div>
  <div class="sidebar-contact">
    <div class="contact-row"><div class="ic"><svg width="20" height="20" viewBox="0 0 20 20"><path d="M4 1l4 4-2 3c1 3 3 5 6 6l3-2 4 4-3 3C8 19 1 12 1 4z" fill="#fff"/></svg></div><div>+91 90210 47315<br>(912) 555-0142</div></div>
    <div class="contact-row"><div class="ic"><svg width="16" height="22" viewBox="0 0 16 22"><path d="M8 0a8 8 0 0 1 8 8c0 6-8 14-8 14S0 14 0 8a8 8 0 0 1 8-8z" fill="#fff"/><circle cx="8" cy="8" r="3" fill="#25a5de"/></svg></div><div>48 Linden Row<br>Fairhaven, MA<br>02719, USA</div></div>
    <div class="contact-row"><div class="ic"><svg width="20" height="14" viewBox="0 0 20 14"><rect width="20" height="14" fill="#fff"/><path d="M0 0l10 8 10-8" fill="none" stroke="#25a5de" stroke-width="1.5"/></svg></div><div>contact@brindavo.com</div></div>
  </div>
</nav>

<section class="school-card" style="top:368px">
  <div class="card-head"><h2 class="card-title" style="font-weight:400">Brindavo School</h2>
    <a class="edit-link">Edit School Profile <svg width="24" height="24" viewBox="0 0 24 24" fill="none" stroke="#222" stroke-width="2.4"><path d="M12 4H3v17h17v-9"/><path d="M9 15l1-4 10-9 2 2-10 9z" fill="#222" stroke-width="1"/></svg></a></div>
  <dl class="card-body">
    <div class="info-row"><dt>Name</dt><span class="sep">:</span><dd>Brindavo School</dd></div>
    <div class="info-row"><dt>School Type</dt><span class="sep">:</span><dd>Grant-maintained school</dd></div>
    <div class="info-row"><dt>School Code</dt><span class="sep">:</span><dd>TeN06934</dd></div>
    <div class="info-row"><dt>School Count</dt><span class="sep">:</span><dd>100</dd></div>
    <div class="info-row"><dt>School Address</dt><span class="sep">:</span><dd>48 Linden Row, Fairhaven MA 02719, USA</dd></div>
    <div class="info-row"><dt>School phone 1&amp;2</dt><span class="sep">:</span><dd>+91 90210 47315, +91 90210 47315</dd></div>
    <div class="info-row"><dt>School Email</dt><span class="sep">:</span><dd>contact@brindavo.in</dd></div>
    <div class="info-row"><dt>School Website</dt><span class="sep">:</span><dd>www.brindavo.in</dd></div>
    <div class="card-logo"><span class="sq"></span>Brindavo</div>
  </dl>
</section>

<section class="school-card" style="top:733px">
  <div class="card-head"><h2 class="card-title" style="font-weight:400">Ashgrove School</h2>
    <a class="edit-link">Edit School Profile <svg width="24" height="24" viewBox="0 0 24 24" fill="none" stroke="#222" stroke-width="2.4"><path d="M12 4H3v17h17v-9"/><path d="M9 15l1-4 10-9 2 2-10 9z" fill="#222" stroke-width="1"/></svg></a></div>
  <dl class="card-body">
    <div class="info-row"><dt>Name</dt><span class="sep">:</span><dd>Ashgrove School</dd></div>
    <div class="info-row"><dt>School Type</dt><span class="sep">:</span><dd>Grant-maintained school</dd></div>
    <div class="info-row"><dt>School Code</dt><span class="sep">:</span><dd>TeN06934</dd></div>
    <div class="info-row"><dt>School Count</dt><span class="sep">:</span><dd>100</dd></div>
    <div class="info-row"><dt>School Address</dt><span class="sep">:</span><dd>48 Linden Row, Fairhaven MA 02719, USA</dd></div>
    <div class="info-row"><dt>School phone 1&amp;2</dt><span class="sep">:</span><dd>+91 90210 47315, +91 90210 47315</dd></div>
    <div class="info-row"><dt>School Email</dt><span class="sep">:</span><dd>contact@brindavo.in</dd></div>
    <div class="info-row"><dt>School Website</dt><span class="sep">:</span><dd>www.brindavo.in</dd></div>
    <div class="card-logo alt"><span class="sq"></span>Ashgrove School</div>
  </dl>
</section>

<footer class="site-footer">
  <p class="copyright">©2014 brindavo , All Rights Reserved.</p>
  <p class="footer-links"><a href="#">Home</a><span>|</span><a href="#">What we do</a><span>|</span><a href="#">Partner with us</a><span>|</span><a href="#">Contact</a></p>
  <div class="social"><i></i><i></i><i></i><i></i></div>
</footer>
</body>
</html>
```